WordPress Classical Pianist Website, one pager with one one-pager as a subsite

Hi everyone,

I'm looking for a long-term freelance designer to refresh and modernize my existing WordPress website (www.talvenor.com).
The new layout should be a clean one-page design with one one-pager subpage (CD's subpage).

From time to time, I also need help with smaller design projects such as concert flyers, CD covers (including booklets), and other promotional materials — that’s why I’m looking for a long-term collaboration.

The website is fully functional; I just need a fresh visual update that matches the style of my new CD and future materials.

Experience with WordPress is essential.
I'm looking for someone reliable, creative, and easy to communicate with — not a large agency.

Thanks a lot!
Roland

Target Market(s)

Classical music audience, concert organizers (!), music students/music universities and piano music lovers worldwide.

Industry/Entity Type

Classical Music / Artist Portfolio

Coding

Coded - Design and coding required

Number of Pages Required

2 page

Font styles to use
Other font styles liked:
• Ephesis Bold, Lexend Tera, Lexend Tera Medium, Adobe Fnt23

Requirements
Must have
• Clean and elegant one-page layout with 1–2 subpages (Bio, Concerts, Contact); high-quality visual design reflecting a professional concert pianist’s identity; visual harmony with my new CD “Ombre sul Lago Fermo” (colors, mood, tone); integration of photos, videos, CD covers, and short audio samples via a mini audio player; all existing content to be transferred from www.talvenor.com ; bilingual structure (German/English); responsive design (desktop + mobile); built on WordPress
Nice to have
• Subtle animations or transitions between sections (smooth scrolling or fade-ins), elegant typography inspired by classical music aesthetics (fonts below), optional dark / light mode design, small music/video player or integrated streaming links (Spotify, Apple Music, YouTube)
Should not have
• Overloaded or cluttered layout, flashy or bright color schemes, stock photos unrelated to piano or classical music, heavy animations or slow loading times, generic, template-looking WordPress themes

```html
<!DOCTYPE html>
<html lang="en">
<head>
<meta charset="utf-8">
<title>Roland Talvenor — Pianist</title>
<link rel="stylesheet" href="https://fonts.googleapis.com/css2?family=Lato:wght@300;400&family=Poppins:wght@300;400;500;600&display=swap">
<style>
:root{
  --gold:#e6b873;
  --gold-light:#f4e2c6;
  --ink:#111111;
  --text:#3a3a3a;
  --muted:#666666;
  --repertoire-bg:#b7dfe6;
  --videos-bg:#7ab4c1;
  --accent:#5aa9bb;
  --white:#ffffff;
  --shadow-grey:#b5b5b5;
  --footer-bg:#0c0c0c;
}
*{box-sizing:border-box;margin:0;padding:0}
html,body{width:1200px;height:4111px;overflow:hidden}
body{font-family:"Poppins",sans-serif;color:var(--text);background:var(--white);position:relative}
.display{font-family:"Lato",sans-serif;font-weight:300;color:var(--ink)}
.btn{position:absolute;display:flex;align-items:center;justify-content:center;background:var(--ink);color:var(--white);font-size:12px;font-weight:500;text-decoration:none}
.section-title{position:absolute;left:0;width:1200px;text-align:center;font-size:34px;letter-spacing:1px}

/* hero */
.hero{position:absolute;top:0;left:0;width:1200px;height:630px;background:linear-gradient(90deg,var(--gold) 0%,#edc990 45%,var(--gold-light) 70%,#e9d9c4 100%)}
.hero-portrait{position:absolute;right:0;top:0;width:560px;height:578px;background:radial-gradient(ellipse at 60% 45%,#c9a07a 0%,#8a6a55 38%,#3a2c27 70%,rgba(30,24,22,.0) 100%)}
.brand{position:absolute;left:160px;top:26px;display:flex;align-items:center;gap:10px;font-family:"Poppins",sans-serif;font-weight:600;font-size:22px;letter-spacing:3px;color:var(--ink)}
.brand-mark{width:12px;height:12px;background:var(--ink)}
.main-nav{position:absolute;top:34px;right:162px;display:flex;gap:38px}
.main-nav a{font-size:12px;color:var(--ink);text-decoration:none;letter-spacing:.3px}
.hero-name{position:absolute;left:156px;top:218px;line-height:1}
.hero-name .first{display:block;font-size:62px;letter-spacing:2px}
.hero-name .last{display:block;font-size:90px;letter-spacing:3px;margin-top:4px}
.keyboard-band{position:absolute;left:0;top:578px;width:1200px;height:52px;background:linear-gradient(180deg,#2a2a2a,#0e0e0e)}

/* biography */
.bio-photo-shadow{position:absolute;left:239px;top:782px;width:383px;height:338px;background:var(--shadow-grey)}
.bio-photo{position:absolute;left:160px;top:707px;width:440px;height:391px;background:linear-gradient(135deg,#d9b98e 0%,#a8805b 45%,#5a4031 100%)}
.bio-heading{position:absolute;left:664px;top:700px;font-size:34px}
.bio-text{position:absolute;left:664px;top:752px;width:372px;font-size:11.6px;line-height:18px;color:var(--text)}
.bio-text strong{font-weight:600;color:var(--ink)}

/* repertoire */
.repertoire{position:absolute;top:1197px;left:0;width:1200px;height:846px;background:var(--repertoire-bg)}
.rep-card{position:absolute;width:423px;height:180px;background:var(--white);box-shadow:0 6px 18px rgba(0,0,0,.06);padding:30px 34px}
.rep-card h3{font-size:20px;font-weight:500;color:var(--ink);margin-bottom:14px}
.rep-card li{list-style:none;font-size:12.6px;line-height:30px;color:var(--muted);padding-left:16px;position:relative}
.rep-card li::before{content:"";position:absolute;left:0;top:13px;width:5px;height:5px;border-radius:50%;background:var(--accent)}

/* press */
.press-item{position:absolute;width:278px}
.press-cover{width:278px;height:276px}
.press-item h3{font-size:16px;font-weight:600;line-height:19px;color:#222;margin-top:22px}
.press-item p{font-size:11.6px;line-height:16.5px;color:var(--muted);margin-top:7px}
.press-item a{display:inline-flex;align-items:center;gap:8px;margin-top:14px;font-size:11.6px;color:#222;text-decoration:underline}

/* videos */
.videos{position:absolute;top:3205px;left:0;width:1200px;height:597px;background:var(--videos-bg)}
.video-grid{position:absolute;left:176px;top:131px;display:grid;grid-template-columns:repeat(4,206px);grid-auto-rows:115px;gap:8px 7.5px}
.video-thumb{background:linear-gradient(160deg,#6b4a2e 0%,#2e2119 55%,#120d0a 100%)}
.video-thumb.stage{background:linear-gradient(170deg,#a58466 0%,#5c4331 50%,#1c1410 100%)}
.video-thumb.dark{background:linear-gradient(160deg,#4a4a4a 0%,#1a1a1a 60%,#0a0a0a 100%)}

/* footer */
.site-footer{position:absolute;top:3802px;left:0;width:1200px;height:309px;background:var(--footer-bg);color:var(--white)}
.footer-brand{position:absolute;left:0;width:1200px;top:42px;display:flex;justify-content:center;align-items:center;gap:12px;font-weight:600;font-size:26px;letter-spacing:4px}
.footer-brand .brand-mark{background:var(--white);width:14px;height:14px}
.footer-nav{position:absolute;top:150px;left:275px;width:740px;display:flex;justify-content:space-between}
.footer-nav a{color:var(--white);font-size:13px;text-decoration:none}
.footer-rule{position:absolute;top:188px;left:185px;width:830px;height:1px;background:#3a3a3a}
.footer-contacts{position:absolute;top:212px;left:295px;display:flex;gap:70px;font-size:12px}
.contact{display:flex;align-items:center;gap:12px}
.contact-icon{width:26px;height:26px;border-radius:50%;background:#6fa9c9;display:flex;align-items:center;justify-content:center}
.social{position:absolute;top:268px;left:0;width:1200px;display:flex;justify-content:center;gap:24px}
.social span{width:11px;height:11px;border-radius:50%;background:var(--white)}
</style>
</head>
<body>

<header class="hero">
  <div class="hero-portrait" role="img" aria-label="Portrait of the pianist resting his chin on his hand, looking to the left"></div>
  <div class="brand"><span class="brand-mark"></span>TALVENOR</div>
  <nav class="main-nav">
    <a href="#">HOME</a><a href="#">BIOGRAPHY</a><a href="#">REPERTOIRE</a><a href="#">PRESS</a><a href="#">MEDIA</a><a href="#">CONTACT</a>
  </nav>
  <h1 class="hero-name display"><span class="first">ROLAND</span><span class="last">TALVENOR</span></h1>
  <div class="keyboard-band" role="img" aria-label="Decorative piano keyboard strip"></div>
</header>

<section class="biography">
  <div class="bio-photo-shadow"></div>
  <div class="bio-photo" role="img" aria-label="Photo of the pianist seated at a grand piano"></div>
  <h2 class="bio-heading display">BIOGRAPHY</h2>
  <p class="bio-text"><strong>Roland Talvenor</strong> , a pianist of international renown, first came to worldwide attention when he won first prize at the prestigious Aldermoor International Piano Competition in 1994. This victory, coupled with the prize for best Chopin interpretation, opened the doors for him to major concert stages in Great Britain, Germany, Italy, Japan and the USA. As a soloist he has performed with renowned orchestras such as the Northgate Symphony Orchestra, The Harrowgate Philharmonic, the Westbay National Orchestra, the Orchestre Régional de Valmont, the Royal Lindqvist Philharmonic Orchestra, the Kerrow Bay Philharmonia Orchestra and the Meridian Coast Symphony Orchestra. He has also worked with outstanding chamber music partners such as the Arden Quartet, the Halvard Quartet, Mira Delacourt, Irina Solvay, Anton Brekke and Lukas Ferrand. These diverse experiences have deepened his understanding of interacting and playing with other musicians and given him a broader artistic perspective.</p>
  <a class="btn" href="#" style="left:665px;top:1087px;width:124px;height:34px">Learn More</a>
</section>

<section class="repertoire">
  <h2 class="section-title display" style="top:52px">REPERTOIRE</h2>
  <div class="rep-card" style="left:169px;top:144px"><h3>WA Mozart (1756 – 1791)</h3><ul><li>Piano Concerto No. 20 in D minor, K. 466</li><li>Piano Concerto No. 21 in C major, K. 467</li><li>Piano Concerto No. 23 in A major, K. 488</li></ul></div>
  <div class="rep-card" style="left:608px;top:144px"><h3>Louis V. Beethoven (1770 – 1827)</h3><ul><li>Piano Concerto No. 1 in C major, op. 15</li><li>Piano Concerto No. 2 in B-flat major, Op. 19</li><li>Piano Concerto No. 3 in C minor, op. 37</li></ul></div>
  <div class="rep-card" style="left:169px;top:342px"><h3>Frederic Chopin (1810 – 1849)</h3><ul><li>Piano Concerto No. 20 in D minor, K. 466</li><li>Piano Concerto No. 21 in C major, K. 467</li><li>Piano Concerto No. 23 in A major, K. 488</li></ul></div>
  <div class="rep-card" style="left:608px;top:342px"><h3>Franz Liszt (1811 – 1886)</h3><ul><li>Piano Concerto No. 1 in C major, op. 15</li><li>Piano Concerto No. 2 in B-flat major, Op. 19</li><li>Piano Concerto No. 3 in C minor, op. 37</li></ul></div>
  <div class="rep-card" style="left:169px;top:540px"><h3>Frederic Chopin (1810 – 1849)</h3><ul><li>Piano Concerto No. 20 in D minor, K. 466</li><li>Piano Concerto No. 21 in C major, K. 467</li><li>Piano Concerto No. 23 in A major, K. 488</li></ul></div>
  <div class="rep-card" style="left:608px;top:540px"><h3>Franz Liszt (1811 – 1886)</h3><ul><li>Piano Concerto No. 1 in C major, op. 15</li><li>Piano Concerto No. 2 in B-flat major, Op. 19</li><li>Piano Concerto No. 3 in C minor, op. 37</li></ul></div>
  <a class="btn" href="#" style="left:520px;top:773px;width:160px;height:34px">View All Repertoire</a>
</section>

<section class="press">
  <h2 class="section-title display" style="top:2080px">PRESS</h2>

  <article class="press-item" style="left:161px;top:2156px">
    <div class="press-cover" role="img" aria-label="CD cover: Beethoven piano sonatas, pianist in black suit on light grey" style="background:linear-gradient(90deg,#3a3a3a 0%,#9a9a9a 40%,#e6e6e6 60%,#ececec 100%)"></div>
    <h3>Sonatas Pathetique,<br>Waldstein, Appassionata</h3>
    <p>Appassionata" means "passionate," and Talvenor stuck to that. He relied entirely on expression. He shaped the first movement with utmost expressiveness and intensity.</p>
    <a href="#">Learn More <svg width="14" height="8" viewBox="0 0 14 8"><path d="M0 4h12M9 1l3 3-3 3" stroke="#222" fill="none" stroke-width="1.2"/></svg></a>
  </article>
  <article class="press-item" style="left:461px;top:2156px">
    <div class="press-cover" role="img" aria-label="CD cover: Russian piano music, pianist at the keyboard in black and white" style="background:linear-gradient(180deg,#1d1d1d 0%,#6a6a6a 40%,#e8e4dc 70%,#bdb5a8 100%)"></div>
    <h3>Scriabin, Rachmaninov,<br>Prokofiev</h3>
    <p>Appassionata" means "passionate," and Talvenor stuck to that. He relied entirely on expression. He shaped the first movement with utmost expressiveness and intensity.</p>
    <a href="#">Learn More <svg width="14" height="8" viewBox="0 0 14 8"><path d="M0 4h12M9 1l3 3-3 3" stroke="#222" fill="none" stroke-width="1.2"/></svg></a>
  </article>
  <article class="press-item" style="left:760px;top:2156px">
    <div class="press-cover" role="img" aria-label="CD cover: Chopin mazurkas, pianist in dark suit on black" style="background:linear-gradient(135deg,#3a3a3a 0%,#151515 55%,#6b6b6b 100%)"></div>
    <h3>Frederic Chopin Edition Vol.<br>10 – Mazurkas</h3>
    <p>Appassionata" means "passionate," and Talvenor stuck to that. He relied entirely on expression. He shaped the first movement with utmost expressiveness and intensity.</p>
    <a href="#">Learn More <svg width="14" height="8" viewBox="0 0 14 8"><path d="M0 4h12M9 1l3 3-3 3" stroke="#222" fill="none" stroke-width="1.2"/></svg></a>
  </article>

  <article class="press-item" style="left:161px;top:2625px">
    <div class="press-cover" role="img" aria-label="CD cover: Chopin sonatas, pianist seated against black" style="background:linear-gradient(160deg,#0d0d0d 0%,#1c1c1c 55%,#4a4a4a 100%)"></div>
    <h3>Sonatas Pathetique,<br>Waldstein, Appassionata</h3>
    <p>Appassionata" means "passionate," and Talvenor stuck to that. He relied entirely on expression. He shaped the first movement with utmost expressiveness and intensity.</p>
    <a href="#">Learn More <svg width="14" height="8" viewBox="0 0 14 8"><path d="M0 4h12M9 1l3 3-3 3" stroke="#222" fill="none" stroke-width="1.2"/></svg></a>
  </article>
  <article class="press-item" style="left:461px;top:2625px">
    <div class="press-cover" role="img" aria-label="CD cover: Chopin preludes and variations, warm orange and green tones" style="background:linear-gradient(180deg,#c7602a 0%,#b9794a 25%,#6f7a4a 60%,#d8b48a 100%)"></div>
    <h3>Scriabin, Rachmaninov,<br>Prokofiev</h3>
    <p>Appassionata" means "passionate," and Talvenor stuck to that. He relied entirely on expression. He shaped the first movement with utmost expressiveness and intensity.</p>
    <a href="#">Learn More <svg width="14" height="8" viewBox="0 0 14 8"><path d="M0 4h12M9 1l3 3-3 3" stroke="#222" fill="none" stroke-width="1.2"/></svg></a>
  </article>
  <article class="press-item" style="left:760px;top:2625px">
    <div class="press-cover" role="img" aria-label="CD cover: Chopin etudes, warm orange and peach tones" style="background:linear-gradient(180deg,#c96a33 0%,#d49468 30%,#e6c3a4 65%,#d9a27a 100%)"></div>
    <h3>Frederic Chopin Edition Vol.<br>10 – Mazurkas</h3>
    <p>Appassionata" means "passionate," and Talvenor stuck to that. He relied entirely on expression. He shaped the first movement with utmost expressiveness and intensity.</p>
    <a href="#">Learn More <svg width="14" height="8" viewBox="0 0 14 8"><path d="M0 4h12M9 1l3 3-3 3" stroke="#222" fill="none" stroke-width="1.2"/></svg></a>
  </article>

  <a class="btn" href="#" style="left:520px;top:3109px;width:160px;height:35px">View All Press</a>
</section>

<section class="videos">
  <h2 class="section-title display" style="top:52px">VIDEOS</h2>
  <div class="video-grid">
    <div class="video-thumb" role="img" aria-label="Video still: pianist with orchestra on stage"></div>
    <div class="video-thumb" role="img" aria-label="Video still: orchestra performing"></div>
    <div class="video-thumb dark" role="img" aria-label="Video still: pianist at a grand piano"></div>
    <div class="video-thumb dark" role="img" aria-label="Video still: pianist playing in dim light"></div>
    <div class="video-thumb" role="img" aria-label="Video still: concert with orchestra"></div>
    <div class="video-thumb" role="img" aria-label="Video still: orchestra and soloist"></div>
    <div class="video-thumb stage" role="img" aria-label="Video still: concert hall with organ"></div>
    <div class="video-thumb dark" role="img" aria-label="Video still: grand piano close-up"></div>
    <div class="video-thumb stage" role="img" aria-label="Video still: pianist on a wooden stage"></div>
    <div class="video-thumb stage" role="img" aria-label="Video still: solo recital on stage"></div>
    <div class="video-thumb" role="img" aria-label="Video still: orchestra seen from above"></div>
    <div class="video-thumb" role="img" aria-label="Video still: full orchestra performance"></div>
  </div>
  <a class="btn" href="#" style="left:520px;top:531px;width:160px;height:34px">View All Videos</a>
</section>

<footer class="site-footer">
  <div class="footer-brand"><span class="brand-mark"></span>TALVENOR</div>
  <nav class="footer-nav">
    <a href="#">Home</a><a href="#">Biography</a><a href="#">Repertoire</a><a href="#">Press</a><a href="#">Media</a><a href="#">Contact</a>
  </nav>
  <div class="footer-rule"></div>
  <div class="footer-contacts">
    <div class="contact"><span class="contact-icon"><svg width="12" height="12" viewBox="0 0 24 24"><path d="M6.6 10.8a15 15 0 006.6 6.6l2.2-2.2a1 1 0 011-.25 11.4 11.4 0 003.6.6 1 1 0 011 1V20a1 1 0 01-1 1A17 17 0 013 4a1 1 0 011-1h3.5a1 1 0 011 1c0 1.25.2 2.45.6 3.6a1 1 0 01-.25 1z" fill="#fff"/></svg></span>+1 555 014 2288</div>
    <div class="contact"><span class="contact-icon"><svg width="12" height="10" viewBox="0 0 24 18"><rect x="1" y="1" width="22" height="16" rx="2" fill="none" stroke="#fff" stroke-width="2"/><path d="M1 2l11 8 11-8" fill="none" stroke="#fff" stroke-width="2"/></svg></span>roland@talvenor.com</div>
    <div class="contact"><span class="contact-icon"><svg width="10" height="13" viewBox="0 0 20 26"><path d="M10 0a9 9 0 00-9 9c0 7 9 17 9 17s9-10 9-17a9 9 0 00-9-9zm0 12.5A3.5 3.5 0 1110 5.5a3.5 3.5 0 010 7z" fill="#fff"/></svg></span>122, Lorem ipsum dolird</div>
  </div>
  <div class="social"><span></span><span></span><span></span></div>
</footer>

</body>
</html>
```